Web Site Design for a Finance (lending) Company

We are opening a new subsidiary that focuses on lending money in the real estate industry. We need a web site designed to represent the business.

The business is lending money to real estate investors. A typical client/borrower will be looking to borrow money to buy a house, renovate it and then sell it at a profit, all within 12 months or less.

Company name is Brevand Finance. Our logo is attached.

Attached is a general outline for the web site. We're working on writing more text for each page but this should give you enough to get started with some ideas.

Competitor web site that I like a lot (as an example): https://quorvelfunding.com/. Many of the general items on this site match what we will need (description of loan programs, FAQ)

Target Market(s)

Real estate investors (generally individuals or small companies with just a few people) who are buying homes, renovating them and then selling them at a profit.

Industry/Entity Type

Finance

Coding

Coded - Design and coding required

Number of Pages Required

5+ page

Colors

Designer to choose colors to be used in the design.

Requirements
Must have
• Minimalist design. Clean lines without too much clutter. Some stock photography is ok but the photos should not be distracting. They should almost fade in to the background so that user can focus on the key information about what our company does instead. We are a finance company, not a design company, so the information about our products will be more interesting to site visitors than the art.
• Some minimalist examples from Snapboard:
• https://www.snapboard-example.com/explore/minimalist-web-design/
Nice to have
• If you search in seekly for "hard money lenders" you will find many examples of web sites from our competition. I have provided a link above to competitor web site that I like a lot.
• I have attached our logo in EPS format. Logo is green. Web site doesn't have to be green but it should be of a color that will work well with the logo.

```html
<!DOCTYPE html>
<html lang="en">
<head>
<meta charset="utf-8">
<title>Brevand Finance — Real Estate Lending</title>
<link href="https://fonts.googleapis.com/css2?family=Bebas+Neue&family=Montserrat:wght@400;500;600;700&family=Raleway:ital,wght@0,300;0,400;0,500;1,300&display=swap" rel="stylesheet">
<style>
:root{
  --yellow:#f0c30f;
  --mint:#d3fbea;
  --dark:#2f2f2f;
  --ink:#333333;
  --muted:#666666;
  --white:#ffffff;
  --hero-green:rgba(62,112,82,.82);
  --footer-bar:#3a3a3a;
  --line:#c9d9d1;
}
*{box-sizing:border-box;margin:0;padding:0}
html,body{width:1200px;height:2586px;overflow:hidden}
body{position:relative;background:var(--white);font-family:'Raleway',sans-serif;color:var(--ink)}
.abs{position:absolute}
a{color:inherit;text-decoration:none}

/* hero */
.hero{left:0;top:0;width:1200px;height:517px;background:linear-gradient(135deg,#4a4a4a 0%,#2c2c2c 45%,#1c1c1c 100%)}
.hero-overlay{left:0;top:0;width:428px;height:517px;background:var(--hero-green)}
.brand{font-family:'Montserrat',sans-serif;font-weight:600;color:var(--white);font-size:19px;line-height:21px;display:flex;align-items:center;gap:10px}
.brand .mark{width:34px;height:34px;border:2px solid var(--white)}
.hero-brand{left:112px;top:28px}
.phone-top{left:980px;top:20px;font-family:'Montserrat',sans-serif;font-weight:600;font-size:14px;color:var(--white);display:flex;align-items:center;gap:7px}
.nav{top:54px;font-family:'Montserrat',sans-serif;font-weight:700;font-size:14px;color:var(--white);letter-spacing:.3px}
.nav.active{color:var(--yellow)}
.hero-frame{left:419px;top:181px;width:310px;height:150px;border:2px solid rgba(255,255,255,.85)}
.headline{left:112px;top:205px;font-family:'Bebas Neue',sans-serif;color:var(--white);font-size:44px;line-height:60px;letter-spacing:1.5px}
.headline .hl{color:var(--yellow);font-size:52px}
.btn-hero{left:112px;top:340px;width:152px;height:39px;background:var(--white);border-bottom:4px solid var(--yellow);font-family:'Montserrat',sans-serif;font-weight:700;font-size:13px;letter-spacing:.5px;color:#222;display:flex;align-items:center;justify-content:center}

/* about */
.about-photo{left:112px;top:578px;width:402px;height:481px;background:linear-gradient(180deg,#ddd6cb 0%,#eee9e1 55%,#cfc8bd 100%)}
.about-panel{left:514px;top:578px;width:370px;height:481px;background:var(--mint)}
.about-title{left:600px;top:620px;font-family:'Montserrat',sans-serif;font-weight:600;font-size:38px;line-height:45px;color:var(--ink);letter-spacing:.5px}
.about-text{left:600px;top:728px;width:480px;font-size:12.5px;line-height:20px;color:#444}
.about-quote{left:640px;top:842px;width:450px;border-left:3px solid #444;padding-left:18px;font-style:italic;font-weight:300;font-size:22px;line-height:30px;color:#444}
.btn-yellow{background:var(--yellow);color:var(--white);font-family:'Montserrat',sans-serif;font-weight:700;font-size:13px;letter-spacing:.5px;display:flex;align-items:center;justify-content:center}
.about-btn{left:600px;top:965px;width:153px;height:42px}

/* loans */
.loans-band{left:0;top:1119px;width:1200px;height:295px;background:var(--yellow)}
.section-title{left:0;width:1200px;text-align:center;font-family:'Montserrat',sans-serif;font-weight:600;font-size:38px}
.loans-title{top:1166px;color:var(--white)}
.loan-card{top:1293px;width:481px;height:302px;background:var(--white);box-shadow:0 3px 10px rgba(0,0,0,.12)}
.loan-art{top:1241px;width:150px;height:148px;border-radius:4px}
.loan-art.house{background:linear-gradient(180deg,#cfcfcf 0%,#f07a68 40%,#ec6e5c 85%,#7cc36a 100%)}
.loan-art.tower{background:linear-gradient(180deg,#e8657a 0%,#38c3dd 25%,#2fb7d2 75%,#9ad46a 100%)}
.loan-mark{top:1398px;width:12px;height:14px;border-left:3px solid var(--yellow);border-right:3px solid var(--yellow)}
.loan-name{top:1428px;width:481px;text-align:center;font-family:'Montserrat',sans-serif;font-weight:600;font-size:24px;color:var(--ink);letter-spacing:.3px}
.loan-desc{top:1468px;width:481px;text-align:center;font-size:14px;line-height:21px;color:var(--muted)}
.btn-outline{border:1px solid #555;background:var(--white);font-family:'Montserrat',sans-serif;font-weight:600;font-size:12px;letter-spacing:.5px;color:#333;display:flex;align-items:center;justify-content:center}
.loan-btn{top:1524px;width:138px;height:34px}

/* resources */
.res-title{top:1646px;color:var(--ink)}
.tabs{left:236px;top:1741px;width:729px;height:36px;border-bottom:2px solid var(--yellow);display:flex}
.tab{height:34px;display:flex;align-items:center;justify-content:center;font-family:'Montserrat',sans-serif;font-weight:600;font-size:14px;letter-spacing:.5px;color:#333}
.tab.active{background:var(--yellow);color:var(--white)}
.post{top:1822px;width:288px;height:266px;background:var(--white);box-shadow:0 2px 10px rgba(0,0,0,.13);padding:12px 8px}
.post-meta{font-family:'Montserrat',sans-serif;font-size:11.5px;font-weight:500;color:#222}
.post-title{margin-top:8px;font-family:'Montserrat',sans-serif;font-weight:600;font-size:17px;line-height:26px;color:#222}
.post-text{margin-top:6px;font-size:12.5px;line-height:22px;color:#555}
.post-more{position:absolute;left:12px;bottom:24px;font-family:'Montserrat',sans-serif;font-weight:700;font-size:13px;color:#222;border-bottom:2px solid #222;letter-spacing:.3px}

/* footer */
.footer{left:0;top:2150px;width:1200px;height:396px;background:var(--mint)}
.footer-brand{left:112px;top:2222px;color:#222;font-size:28px;line-height:32px}
.footer-brand .mark{width:52px;height:52px;border:3px solid #222}
.footer-phone{left:112px;top:2340px;font-family:'Montserrat',sans-serif;font-weight:700;font-size:38px;color:#222;letter-spacing:1px}
.footer-address{left:112px;top:2392px;font-size:19px;line-height:31px;color:#444}
.foot-link{left:467px;width:271px;height:30px;border-bottom:1px solid #b5c9bf;font-size:19px;color:#444;display:flex;align-items:center;gap:6px}
.field{left:845px;width:265px;border:1px solid #9ed8bd;background:transparent;font-size:12px;color:#444;padding:6px 8px}
.send{left:845px;top:2441px;width:265px;height:33px;font-size:12px}
.copyright{left:0;top:2546px;width:1200px;height:40px;background:var(--footer-bar);color:#e6e6e6;font-size:12px;display:flex;align-items:center;justify-content:center;gap:4px}
.copyright .name{color:var(--yellow);border-bottom:1px solid var(--yellow);font-size:14px}
</style>
</head>
<body>

<!-- Hero -->
<header>
  <div class="abs hero" role="img" aria-label="Evening photograph of a large two-storey house with a pool in the foreground"></div>
  <div class="abs hero-overlay"></div>
  <div class="abs brand hero-brand"><span class="mark"></span><span>Brevand<br>Finance</span></div>
  <div class="abs phone-top">
    <svg width="12" height="12" viewBox="0 0 24 24" aria-hidden="true"><path fill="#fff" d="M6.6 10.8a15.1 15.1 0 0 0 6.6 6.6l2.2-2.2a1 1 0 0 1 1-.25 11.4 11.4 0 0 0 3.6.57 1 1 0 0 1 1 1V20a1 1 0 0 1-1 1A17 17 0 0 1 3 4a1 1 0 0 1 1-1h3.5a1 1 0 0 1 1 1c0 1.25.2 2.45.57 3.6a1 1 0 0 1-.25 1z"/></svg>
    123-456-789
  </div>
  <a class="abs nav active" style="left:552px">HOME</a>
  <a class="abs nav" style="left:641px">ABOUT US</a>
  <a class="abs nav" style="left:762px">LOANS</a>
  <a class="abs nav" style="left:858px">RESOURSES</a>
  <a class="abs nav" style="left:993px">CONTACT US</a>
  <div class="abs hero-frame"></div>
  <h1 class="abs headline">Local <span class="hl">Real Estate</span> Experts <span class="hl">Lending</span> to<br>Local <span class="hl">Real Estate</span> Investors</h1>
  <a class="abs btn-hero">LEARN MORE</a>
</header>

<!-- About -->
<section>
  <div class="abs about-photo" role="img" aria-label="Bright living room with chandelier, fireplace and white sofa"></div>
  <div class="abs about-panel"></div>
  <h2 class="abs about-title">About<br>Brevand Finance</h2>
  <p class="abs about-text">Lorem ipsum dolor sit amet, consectetur adipiscing elit, sed do eiusmod tempor incididunt ut labore et dolore magna aliqua. Ut enim ad minim veniam, quis nostrud exercitation ullamco laboris nisi ut aliquip ex ea commodo consequat. Duis aute irure dolor in reprehenderit in voluptate.</p>
  <blockquote class="abs about-quote">Dolor sit amet, consectetur adipiscing elit, sed do eiusmod tempor incididunt ut labore et dolore magna aliqua.</blockquote>
  <a class="abs btn-yellow about-btn">LEARN MORE</a>
</section>

<!-- Loans -->
<section>
  <div class="abs loans-band"></div>
  <h2 class="abs section-title loans-title">Loans</h2>

  <div class="abs loan-card" style="left:112px"></div>
  <div class="abs loan-art house" style="left:278px" role="img" aria-label="Illustration of a red house with trees"></div>
  <div class="abs loan-mark" style="left:346px"></div>
  <h3 class="abs loan-name" style="left:112px">Fix and Flip Loans</h3>
  <p class="abs loan-desc" style="left:112px">Sed ut perspiciatis unde omnis iste natus error sit volu<br>tatem accusantium doloremque laudantium.</p>
  <a class="abs btn-outline loan-btn" style="left:288px">VIEW DETAILS</a>

  <div class="abs loan-card" style="left:607px"></div>
  <div class="abs loan-art tower" style="left:773px" role="img" aria-label="Illustration of a blue office tower with trees"></div>
  <div class="abs loan-mark" style="left:841px"></div>
  <h3 class="abs loan-name" style="left:607px">Commercial Hard Money Loans</h3>
  <p class="abs loan-desc" style="left:607px">Sed ut perspiciatis unde omnis iste natus error sit volu<br>tatem accusantium doloremque laudantium.</p>
  <a class="abs btn-outline loan-btn" style="left:783px">VIEW DETAILS</a>
</section>

<!-- Resources -->
<section>
  <h2 class="abs section-title res-title">Resources</h2>
  <nav class="abs tabs">
    <span class="tab active" style="width:150px">BLOG</span>
    <span class="tab" style="width:200px">NEWS</span>
    <span class="tab" style="width:160px">SERVICES</span>
    <span class="tab" style="width:150px">TESTIMONIALS</span>
  </nav>

  <article class="abs post" style="left:112px">
    <div class="post-meta">by Brevand&nbsp; 3 hour ago</div>
    <h4 class="post-title">Lorem ipsum dolor sit amet, consectetur adipiscing elit</h4>
    <p class="post-text">Lorem ipsum dolor sit amet, consectetur adipiscing elit, sed do eiusmod tempor incididunt ut labore et dolore magna aliqua. Ut enim ad minim veniam, quis nostrud exercitation ullamco .</p>
    <a class="post-more">READ MORE</a>
  </article>
  <article class="abs post" style="left:455px">
    <div class="post-meta">by Brevand&nbsp; 3 hour ago</div>
    <h4 class="post-title">Lorem ipsum dolor sit amet, consectetur adipiscing elit</h4>
    <p class="post-text">Lorem ipsum dolor sit amet, consectetur adipiscing elit, sed do eiusmod tempor incididunt ut labore et dolore magna aliqua. Ut enim ad minim veniam, quis nostrud exercitation ullamco .</p>
    <a class="post-more">READ MORE</a>
  </article>
  <article class="abs post" style="left:800px">
    <div class="post-meta">by Brevand&nbsp; 3 hour ago</div>
    <h4 class="post-title">Lorem ipsum dolor sit amet, consectetur adipiscing elit</h4>
    <p class="post-text">Lorem ipsum dolor sit amet, consectetur adipiscing elit, sed do eiusmod tempor incididunt ut labore et dolore magna aliqua. Ut enim ad minim veniam, quis nostrud exercitation ullamco .</p>
    <a class="post-more">READ MORE</a>
  </article>
</section>

<!-- Footer -->
<footer>
  <div class="abs footer"></div>
  <div class="abs brand footer-brand"><span class="mark"></span><span>Brevand<br>Finance</span></div>
  <div class="abs footer-phone">123-456-789</div>
  <address class="abs footer-address" style="font-style:normal">4567 Lorem Rd Ste 0-123<br>Ipsum Dolar, GA 123456</address>

  <a class="abs foot-link" style="top:2225px">› Commercial Loans</a>
  <a class="abs foot-link" style="top:2279px">› Residential Loans</a>
  <a class="abs foot-link" style="top:2333px">› Fix &amp; Flip Loans</a>
  <a class="abs foot-link" style="top:2387px">› Call 123-456-789</a>

  <div class="abs field" style="top:2233px;height:34px">Name</div>
  <div class="abs field" style="top:2274px;height:34px">Email</div>
  <div class="abs field" style="top:2314px;height:34px">Phone</div>
  <div class="abs field" style="top:2355px;height:78px">Message</div>
  <a class="abs btn-yellow send">SEND</a>

  <div class="abs copyright">© 2017 Copyright <span class="name">Brevand Finance</span>. ALl Rights Reserved.</div>
</footer>

</body>
</html>
```